Book Cover needed - Disinformation and fake news

I need a book cover (front, back, spine) for the 1st edition of a book entitled ‘Marea Silenciosa’ (Means – Silent Tide) and subtitled ‘Los ecos que nadie quiso escuchar’ (Means - The echoes nobody wanted to hear) (inverted commas not to be part of the title and subtitle). The author is ‘Tomás Herreruela’. The finished size of the paperback version will be 5.25" x 8". There will be paperback and e-book versions, so 2 covers will need to be provided: one for the e-book version just with the front cover, and the full book cover for the paperback version.
The final number of pages is expected to be in the region of 350-500 pages. Text for the back cover is down below, and at the bottom of the back cover should have space for the ISBN bar code on the right. The books will be published with PQN - Velmora, so should follow their indications for any specification needed.
The topics discussed include disinformation, fake news, psychological operations. Feel free to design the cover based on those. The design should be original and not include any stock images that have been created by someone else or may require obtaining a copyright license to use.
Back Cover Text (spacing should be respected) :
Oficina del consenso, desinformación, “fake news”... en los últimos años nos hemos visto envueltos en una discusión pública rodeados de estos términos sin terminar de entender exactamente qué significan y lo que es peor, sin saber que realmente nos rodean desde que el hombre es hombre.
En esta obra el autor busca acercanos al mundo de la Marea Silenciosa, aquellas operaciones que buscan influir sobre el comportamiento de la población. Sin hacer uso de un lenguaje excesivamente técnico relata como la evolución de la naturaleza de la guerra a los parámetros del siglo XXI promueve un enfoque del conflicto que no supone un uso de la fuerza tradicional. ¿Para qué atacar las instituciones de un país de forma directa, cuando puedes fomentar el conflicto social entre grupos antagónicos y desestabilizar sin realizar un solo disparo?
¿Cómo razona el ser humano? ¿Son nuestras ideas tan nuestras como creemos? ¿Por qué importa tanto el uso preciso del lenguaje a la hora de comunicarnos?, ¿Cómo nos afectan las razones y emociones de los demás? ¿Por qué tendemos a prestar mayor atención a argumentos que encajen con nuestras propias ideas? ¿Cómo nos afecta la conversación en redes sociales?
Armados con el conocimiento que reside en este libro, quizás, seamos menos susceptibles de caer bajo la influencia de grupos con intereses espurios.
General public with an interest on disinformation - fake news

```html
<!DOCTYPE html>
<html lang="es">
<head>
<meta charset="utf-8">
<title>Marea Silenciosa — Tomás Herreruela</title>
<link rel="stylesheet" href="https://fonts.googleapis.com/css2?family=Bebas+Neue&family=Oswald:wght@500&display=swap">
<style>
  :root {
    --page: #ffffff;
    --cover-top: #0b1d63;
    --cover-mid: #05103a;
    --cover-bottom: #01030c;
    --title-blue: #2ba3f7;
    --title-glow: rgba(43, 163, 247, 0.45);
    --text-white: #ffffff;
    --art-core: #7fd8ff;
    --art-mid: #1f6fd6;
    --art-edge: #0a2a7a;
  }
  * { margin: 0; padding: 0; box-sizing: border-box; }
  html, body {
    width: 1200px;
    height: 1200px;
    overflow: hidden;
    background: var(--page);
  }
  .book-cover {
    position: absolute;
    left: 241px;
    top: 60px;
    width: 719px;
    height: 1080px;
    background: linear-gradient(180deg, var(--cover-top) 0%, var(--cover-mid) 30%, var(--cover-bottom) 100%);
    overflow: hidden;
    text-align: center;
  }
  .title {
    position: absolute;
    left: 0;
    right: 0;
    top: 48px;
    font-family: "Bebas Neue", "Oswald", sans-serif;
    font-weight: 400;
    font-size: 166px;
    line-height: 168px;
    letter-spacing: 3px;
    color: var(--title-blue);
    text-shadow: 0 0 22px var(--title-glow);
  }
  .title span { display: block; }
  .subtitle {
    position: absolute;
    left: 0;
    right: 0;
    top: 446px;
    font-family: "Oswald", sans-serif;
    font-weight: 500;
    font-size: 27px;
    letter-spacing: 1.5px;
    color: var(--text-white);
    text-transform: uppercase;
  }
  .cover-art {
    position: absolute;
    left: 159px;
    top: 519px;
    width: 425px;
    height: 500px;
  }
  .author {
    position: absolute;
    left: 0;
    right: 0;
    top: 1030px;
    transform: translateY(-100%);
    font-family: "Oswald", sans-serif;
    font-weight: 500;
    font-size: 52px;
    letter-spacing: 5px;
    color: var(--text-white);
    text-transform: uppercase;
  }
</style>
</head>
<body>
  <main class="book-cover">
    <h1 class="title"><span>Marea</span><span>Silenciosa</span></h1>
    <p class="subtitle">Los ecos que nadie quiso escuchar</p>
    <svg class="cover-art" viewBox="0 0 425 500" role="img" aria-label="Glowing translucent blue brain seen from the front, with a battle scene of silhouetted soldiers and red and blue smoke across its middle">
      <defs>
        <radialGradient id="brainGlow" cx="50%" cy="45%" r="55%">
          <stop offset="0%" stop-color="var(--art-core)"/>
          <stop offset="55%" stop-color="var(--art-mid)"/>
          <stop offset="100%" stop-color="var(--art-edge)" stop-opacity="0.6"/>
        </radialGradient>
      </defs>
      <ellipse cx="212" cy="240" rx="205" ry="230" fill="url(#brainGlow)"/>
    </svg>
    <p class="author">Tomás Herreruela</p>
  </main>
</body>
</html>
```